Brightmoor Partners Branding Revamp

We are a consulting company, looking for a way to display and promote our brand. We have 2 sides to the business- Brightmoor (financial) and Partners (cyber security). The financial side products relate to business necessities: card processing, website design/hosting/maintenance, VoIP phone systems. The cyber security side promotes a bundled package of 4 solutions: network vulnerability scan, dark web scan, anti-ransomeware/malware software, and image-level backups. We want people to understand that partnering with Brightmoor Partners gives them “Elevated Peace of Mind” (tagline). Current badge and logos uploaded.

Target Market(s)

Small businesses

Contact Information for Business Card

Lena Marwick, Vice President, lena@brightmoorpartners.example, 555-806-1937, www.brightmoorpartners.example

Requirements
Nice to have
• I do prefer the darker background for front and back

```html
<!DOCTYPE html>
<html lang="en">
<head>
<meta charset="utf-8">
<title>Brightmoor Partners – Business Card</title>
<link rel="stylesheet" href="https://fonts.googleapis.com/css2?family=Montserrat:wght@400;600&display=swap">
<style>
  :root {
    --backdrop: #d4d4d4;
    --card: #1c1c1c;
    --card-top: #262626;
    --accent: #e2322b;
    --ink: #f2f2f2;
    --ink-soft: #d9d9d9;
  }
  * { box-sizing: border-box; margin: 0; padding: 0; }
  html, body { width: 1200px; height: 800px; overflow: hidden; }
  body {
    background: var(--backdrop);
    font-family: "Montserrat", sans-serif;
    display: flex;
    align-items: center;
    justify-content: center;
    gap: 50px;
  }
  .card {
    width: 525px;
    height: 300px;
    background: linear-gradient(160deg, var(--card-top) 0%, var(--card) 55%);
    border-radius: 3px;
    box-shadow: 0 18px 40px rgba(0,0,0,0.35);
    position: relative;
  }
  /* Front */
  .card--front {
    display: flex;
    align-items: center;
    justify-content: center;
  }
  .brand {
    display: flex;
    align-items: center;
    gap: 14px;
  }
  .brand__mark {
    width: 16px;
    height: 16px;
    background: var(--accent);
  }
  .brand__name {
    color: var(--ink);
    font-weight: 600;
    letter-spacing: 0.22em;
    text-transform: uppercase;
    line-height: 1.35;
  }
  .card--front .brand__name { font-size: 22px; }
  /* Back */
  .card--back {
    display: flex;
    align-items: center;
    justify-content: space-between;
    padding: 0 34px;
  }
  .contact__name {
    color: var(--accent);
    font-size: 17px;
    font-weight: 400;
    letter-spacing: 0.04em;
    text-transform: uppercase;
  }
  .contact__title {
    color: var(--ink-soft);
    font-size: 11px;
    letter-spacing: 0.2em;
    text-transform: uppercase;
    margin: 3px 0 14px;
  }
  .contact__list { list-style: none; }
  .contact__item {
    display: flex;
    align-items: center;
    gap: 7px;
    color: var(--ink-soft);
    font-size: 10.5px;
    letter-spacing: 0.03em;
    margin-bottom: 5px;
  }
  .contact__icon { width: 10px; height: 10px; flex: none; }
  .card--back .brand__name { font-size: 15px; }
</style>
</head>
<body>
  <section class="card card--front" aria-label="Card front">
    <div class="brand">
      <span class="brand__mark"></span>
      <span class="brand__name">Brightmoor<br>Partners</span>
    </div>
  </section>

  <section class="card card--back" aria-label="Card back">
    <div class="contact">
      <h1 class="contact__name">Lena Marwick</h1>
      <p class="contact__title">Vice President</p>
      <ul class="contact__list">
        <li class="contact__item">
          <svg class="contact__icon" viewBox="0 0 10 10"><rect x="0.5" y="2" width="9" height="6" fill="none" stroke="#e2322b" stroke-width="1"/><path d="M0.5 2 L5 5.5 L9.5 2" fill="none" stroke="#e2322b" stroke-width="1"/></svg>
          lena@brightmoorpartners.example
        </li>
        <li class="contact__item">
          <svg class="contact__icon" viewBox="0 0 10 10"><path d="M2.2 0.8 L3.8 2.6 L2.9 3.8 Q4 6 6.2 7.1 L7.4 6.2 L9.2 7.8 L8 9.3 Q3.5 8.8 0.7 2 Z" fill="#e2322b"/></svg>
          555-806-1937
        </li>
        <li class="contact__item">
          <svg class="contact__icon" viewBox="0 0 10 10"><circle cx="5" cy="5" r="4.4" fill="none" stroke="#e2322b" stroke-width="1"/><ellipse cx="5" cy="5" rx="1.9" ry="4.4" fill="none" stroke="#e2322b" stroke-width="0.8"/><line x1="0.6" y1="5" x2="9.4" y2="5" stroke="#e2322b" stroke-width="0.8"/></svg>
          www.brightmoorpartners.example
        </li>
      </ul>
    </div>
    <div class="brand">
      <span class="brand__mark"></span>
      <span class="brand__name">Brightmoor<br>Partners</span>
    </div>
  </section>
</body>
</html>
```